CRPG is needing business cards, and stationary created.

Pixel Forge created a logo for our business, and now we are wanting business cards, and stationary. I have included two designs of the same logo. Please feel free to use them as you want. The name of the company is Cedar Ridge Property Group LLC, the address is 812 NE Willow Ln., Suite 9, the city & state is Bend, Oregon, zip code is 97815, Telephone number is 541-327-4489, Fax number is 541-327-6051, the name on the business card is Carl Whitby CMCA

Industry/Entity Type

Property Management

Contact Information for Business Card

The card needs to look professional. Upscale.

Requirements
Must have
• The colors we are using are on the logo that has been uploaded.

```html
<!DOCTYPE html>
<html lang="en">
<head>
<meta charset="utf-8">
<title>Cedar Ridge Property Group – Business Card</title>
<link href="https://fonts.googleapis.com/css2?family=Exo+2:wght@500;700&family=Roboto+Condensed:wght@400;700&display=swap" rel="stylesheet">
<style>
  :root {
    --backdrop: #2a2a2b;
    --navy: #3a4a5c;
    --navy-deep: #334252;
    --teal: #1b8a72;
    --paper: #f3f3f2;
    --ink: #3a4452;
    --white: #ffffff;
  }
  * { margin: 0; padding: 0; box-sizing: border-box; }
  html, body { width: 1200px; height: 852px; overflow: hidden; }
  body { background: var(--backdrop); position: relative; font-family: "Roboto Condensed", sans-serif; }

  .card {
    position: absolute;
    width: 520px;
    height: 300px;
    border-radius: 22px;
    overflow: hidden;
  }
  .card-back {
    left: 80px; top: 110px;
    background: var(--navy);
    display: flex; align-items: center; justify-content: center;
  }
  .back-mark {
    font-family: "Exo 2", sans-serif;
    font-weight: 700;
    font-size: 30px;
    letter-spacing: 3px;
    color: var(--navy-deep);
    display: flex; align-items: center; gap: 14px;
    text-transform: uppercase;
  }
  .back-mark .mark-square { width: 34px; height: 34px; background: var(--navy-deep); }

  .card-front { left: 600px; top: 440px; background: var(--paper); }
  .front-wave { position: absolute; inset: 0; }

  .holder { position: absolute; right: 34px; top: 26px; text-align: right; }
  .holder-name {
    font-family: "Exo 2", sans-serif; font-weight: 700;
    font-size: 21px; letter-spacing: 1px; color: var(--ink); line-height: 1.1;
  }
  .holder-credential { font-size: 11px; color: var(--teal); letter-spacing: 1px; margin-top: 2px; }

  .address {
    position: absolute; right: 34px; top: 76px;
    text-align: right; font-size: 13px; line-height: 1.35; color: var(--ink);
  }

  .contact {
    position: absolute; right: 28px; top: 162px;
    list-style: none; text-align: right;
    font-size: 12.5px; line-height: 1.55; color: var(--white);
  }
  .contact li { display: flex; justify-content: flex-end; align-items: center; gap: 7px; }
  .contact svg { width: 11px; height: 11px; fill: var(--white); }

  .brand { position: absolute; left: 34px; top: 168px; display: flex; align-items: center; gap: 12px; }
  .brand-square { width: 30px; height: 30px; background: var(--teal); }
  .brand-name {
    font-family: "Exo 2", sans-serif; font-weight: 700;
    color: var(--teal); text-transform: uppercase;
    font-size: 24px; line-height: 1; letter-spacing: 1px;
  }
  .brand-name small { display: block; font-size: 11px; letter-spacing: 4px; margin-top: 5px; }
  .brand-tagline {
    position: absolute; left: 76px; top: 222px;
    font-family: "Roboto Condensed", sans-serif; font-weight: 700;
    color: var(--teal); font-size: 9px; letter-spacing: 5px; text-transform: uppercase;
  }
</style>
</head>
<body>

<section class="card card-back" aria-label="Card back">
  <div class="back-mark"><span class="mark-square"></span>Cedar Ridge</div>
</section>

<section class="card card-front" aria-label="Card front">
  <svg class="front-wave" viewBox="0 0 520 300" preserveAspectRatio="none" aria-hidden="true">
    <path d="M520 142 C430 142 380 160 340 200 C300 245 220 284 0 290 L0 300 L520 300 Z" fill="var(--navy)"/>
    <path d="M520 128 C425 128 370 148 328 188 C288 232 210 270 10 274" fill="none" stroke="var(--teal)" stroke-width="6"/>
  </svg>

  <div class="holder">
    <div class="holder-name">CARL WHITBY</div>
    <div class="holder-credential">CMCA</div>
  </div>

  <p class="address">812 NE Willow Ln., Suite 9,<br>Bend, Oregon 97815</p>

  <ul class="contact">
    <li>541-327-4489
      <svg viewBox="0 0 12 12"><path d="M2 1h2.5l1 3-1.5 1a6 6 0 0 0 3 3l1-1.5 3 1V10a1 1 0 0 1-1 1A9 9 0 0 1 1 2a1 1 0 0 1 1-1z"/></svg></li>
    <li>541-327-6051
      <svg viewBox="0 0 12 12"><path d="M3 1h5v3H3zM1 5h10v5H9V8H3v2H1zM3 9h6v2H3z"/></svg></li>
    <li>www.cedarridgegroup.com
      <svg viewBox="0 0 12 12"><circle cx="6" cy="6" r="5" fill="none" stroke="#fff" stroke-width="1.2"/><path d="M1 6h10M6 1v10" stroke="#fff" stroke-width="1"/></svg></li>
    <li>carl@cedarridgegroup.com
      <svg viewBox="0 0 12 12"><path d="M1 3h10v6H1z" fill="none" stroke="#fff" stroke-width="1.2"/><path d="M1 3l5 4 5-4" fill="none" stroke="#fff" stroke-width="1.2"/></svg></li>
  </ul>

  <div class="brand">
    <span class="brand-square"></span>
    <div class="brand-name">Cedar Ridge<small>Property Group</small></div>
  </div>
  <div class="brand-tagline">Built On Trust</div>
</section>

</body>
</html>
```